Circulation Rub tube and carton design

We will be launching 3 heat/soothing/circulation rubs, (intense for sports, relaxing for muscles and soothing for aches) and need a portfolio of tube and carton designs to launch with. The product name will be Velmora (Logo Required) and all 3 products will contain Arginine, which is a key feature of the product. We would like to see a bold designs but using earthy tones. Will need an information/ingredients panel on back of tube and carton. Have attached market examples of similar products.
Updates

It will need the following text included 100gm With Arginine for supporting circulation aiding in the temporary relief of Joint and Muscular Pain Joint and Muscular inflammation Stiff Joints Spains, strains, sporting injuries Mild Arthritis

Target Market(s)

there are 3 variants, they will be aimed at 3 different markets. 1. Brelt Intense - for sports 2. Brelt Relax - General population 3. Brelt Soothe - Aged population (arthritis, aches)

Requirements
Must have
• Text to be included 2 separate areas - 100gm & - With Arginine for supporting circulation aiding in the temporary relief of Joint and Muscular Pain Joint and Muscular inflammation Stiff Joints Spains, strains, sporting injuries Mild Arthritis

```html
<!DOCTYPE html>
<html lang="en">
<head>
<meta charset="utf-8">
<title>Brelt Soothe – Carton Front</title>
<link href="https://fonts.googleapis.com/css2?family=PT+Serif:wght@400;700&family=PT+Sans+Narrow&display=swap" rel="stylesheet">
<style>
  :root {
    --canvas: #ffffff;
    --panel: #e5e3e0;
    --navy: #4f5c79;
    --ink: #262626;
    --white: #ffffff;
    --rule: #8898aa;
  }
  * { margin: 0; padding: 0; box-sizing: border-box; }
  html, body {
    width: 1200px; height: 1200px; overflow: hidden;
    background: var(--canvas);
  }
  .carton-front {
    position: absolute;
    left: 370px; top: 40px;
    width: 460px; height: 1120px;
    background: var(--panel);
    color: var(--ink);
  }
  .maker {
    position: absolute;
    left: 0; width: 100%; top: 220px;
    display: flex; align-items: center; justify-content: center;
    gap: 14px;
  }
  .maker-square {
    width: 26px; height: 26px;
    background: var(--navy);
  }
  .maker-name {
    font-family: "PT Serif", serif;
    font-weight: 400;
    font-size: 40px;
    line-height: 1;
    color: var(--ink);
  }
  .product-name {
    position: absolute;
    left: 0; width: 100%; top: 430px;
    text-align: center;
    font-family: "PT Serif", serif;
    font-weight: 700;
    font-size: 62px;
    line-height: 1.1;
    color: var(--ink);
  }
  .net-weight {
    position: absolute;
    left: 50%; transform: translateX(-50%);
    top: 650px;
    width: 166px; height: 58px;
    background: var(--navy);
    color: var(--white);
    font-family: "PT Serif", serif;
    font-weight: 700;
    font-size: 44px;
    line-height: 58px;
    text-align: center;
  }
  .key-ingredient {
    position: absolute;
    left: 0; width: 100%; top: 722px;
    text-align: center;
    font-family: "PT Serif", serif;
    color: var(--ink);
  }
  .key-ingredient .with { display: block; font-size: 34px; line-height: 44px; }
  .key-ingredient .ingredient { display: block; font-weight: 700; font-size: 54px; line-height: 62px; }
  .divider {
    position: absolute;
    left: 50%; transform: translateX(-50%);
    top: 858px;
    width: 194px; height: 7px;
    background: var(--rule);
  }
  .benefits {
    position: absolute;
    left: 80px; top: 892px;
    width: 300px;
    font-family: "PT Sans Narrow", sans-serif;
    font-size: 20px;
    line-height: 25px;
    color: var(--ink);
  }
  .benefits-intro { text-align: justify; text-align-last: left; }
  .benefit-list {
    list-style: none;
    margin-top: 2px;
    border-left: 4px solid var(--navy);
    padding-left: 8px;
  }
  .benefit-list li::before { content: "· "; }
  .base-band {
    position: absolute;
    left: 0; bottom: 0;
    width: 100%; height: 38px;
    background: var(--navy);
  }
</style>
</head>
<body>
  <main class="carton-front">
    <div class="maker">
      <span class="maker-square"></span>
      <span class="maker-name">Velmora</span>
    </div>

    <h1 class="product-name">Brelt Soothe</h1>

    <div class="net-weight">100 gm</div>

    <p class="key-ingredient">
      <span class="with">with</span>
      <span class="ingredient">Arginine</span>
    </p>

    <div class="divider"></div>

    <section class="benefits">
      <p class="benefits-intro">With ARGININE for supporting circulation aiding in the temporary relief of:</p>
      <ul class="benefit-list">
        <li>Joint and Muscular Pain</li>
        <li>Joint and Muscular inflammation</li>
        <li>Stiff Joints</li>
        <li>Spains, strains, sporting injuries</li>
        <li>Mild Arthritis</li>
      </ul>
    </section>

    <div class="base-band"></div>
  </main>
</body>
</html>
```